Vastmere Holdings Webpage Design

We need a new website for our company. The company is Vastmere Holdings Pty Ltd. We are in the business of Asbestos Removal; Demolition; Earthworks and Transport. We do not advertise and would like our website to be a reference point for our clients / potential clients and also to make our services known to those searching the internet for the services we offer. Some examples of the style of website we are after are:
http://www.quorrintdemolition.com.au/
http://m.feltrovindemolitions.com.au/
http://www.pinsettodemolition.com.au
http://www.rulqa.com.au
http://www.tjhservices.com.au
http://www.steadfield-deconstruction.com.au
We will need to work on content. Enclosed is an example. We also need to purchase the domain vastmereholdings.com.au and need to set up email accounts and ensure the website is mobile friendly. We have a company logo and have built our business on delivering professional, quality services on time. We would like the webpage to be simple, informative and professional - black and white / grey themed. We would also like to add a photo gallery etc later.

Industry/Entity Type

Construction

Coding

Coded - Design and coding required

Number of Pages Required

1 page

Colors
000000
fcfcfc
959595
dddddd

Requirements
Must have
• Information regarding the services we provide

```html
<!DOCTYPE html>
<html lang="en">
<head>
<meta charset="utf-8">
<title>Vastmere Holdings</title>
<link rel="stylesheet" href="https://fonts.googleapis.com/css2?family=Fira+Sans+Condensed:wght@400;500&family=Roboto:wght@400;500&display=swap">
<style>
:root{
  --black:#000000;
  --ink:#111111;
  --white:#fcfcfc;
  --grey:#959595;
  --light:#dddddd;
  --text:#333333;
  --muted:#8a8a8a;
}
*{box-sizing:border-box;margin:0;padding:0}
html,body{width:1200px;height:2740px;overflow:hidden;background:var(--white)}
body{font-family:"Roboto",Arial,sans-serif;color:var(--text);position:relative}
.head{font-family:"Fira Sans Condensed","Arial Narrow",sans-serif;font-weight:500;text-transform:uppercase;letter-spacing:1px}
section,header{position:absolute;left:0;width:1200px;overflow:hidden}
.abs{position:absolute}
.center{text-align:center}

/* top bar */
.topbar{top:0;height:44px;background:var(--black);color:var(--light);font-size:11.5px;display:flex;justify-content:flex-end;align-items:center;padding-right:112px;gap:18px}
.topbar .contact{display:flex;gap:16px;align-items:center;white-space:nowrap}
.topbar .contact span{display:flex;gap:5px;align-items:center}
.quote-btn{flex:none;height:32px;padding:0 14px;background:var(--light);color:var(--ink);font-size:11px;line-height:32px;border-radius:3px;font-weight:500;white-space:nowrap}

/* nav */
.nav{top:44px;height:80px;background:var(--white);border-bottom:1px solid var(--light)}
.logo{position:absolute;left:110px;top:22px;font-family:"Fira Sans Condensed",sans-serif;color:var(--ink);font-size:26px;letter-spacing:4px;line-height:1}
.logo small{display:block;font-size:9px;letter-spacing:6px;text-align:center;margin-top:3px;color:var(--ink)}
.menu{position:absolute;right:110px;top:34px;display:flex;gap:44px;font-size:12px;color:var(--text);align-items:center}
.menu .active{color:var(--ink);font-weight:500;border-bottom:1px solid var(--ink);padding-bottom:3px;position:relative}
.menu .active::before{content:"";position:absolute;left:-28px;top:7px;width:22px;height:1px;background:var(--ink)}

/* hero */
.hero{top:124px;height:508px}
.hero-photo{position:absolute;inset:0;background:linear-gradient(135deg,#5a534a 0%,#7b7262 30%,#4a453e 60%,#2b2926 100%)}
.hero-shade{position:absolute;inset:0;background:rgba(0,0,0,.25)}
.hero h1{position:absolute;top:220px;width:100%;font-size:46px;color:var(--white);font-weight:400}
.dots{position:absolute;display:flex;gap:9px}
.hero .dots{top:303px;left:570px}
.dots i{width:11px;height:11px;border-radius:50%;border:2px solid var(--white)}
.dots i.on{background:var(--white)}
.feature-badge{position:absolute;top:348px;width:140px;height:140px;margin-left:-70px;border-radius:50%;background:var(--ink);color:var(--white);text-align:center;font-size:14px}
.feature-badge svg{display:block;margin:34px auto 12px}

/* features */
.features{top:632px;height:217px;background:var(--black)}
.col{position:absolute;width:310px;margin-left:-155px;text-align:center}
.features p{color:var(--light);font-size:12px;line-height:26px;top:40px}
.btn{position:absolute;width:110px;height:46px;margin-left:-55px;border:1px solid currentColor;font-size:12px;text-align:center;line-height:44px;letter-spacing:1px}
.features .btn{top:131px;color:var(--white)}

/* about */
.about{top:849px;height:329px}
.about-bg{position:absolute;inset:0;background:linear-gradient(160deg,#2a2a2a,#161616 55%,#0b0b0b)}
.about h2{position:absolute;top:82px;width:100%;color:var(--white);font-size:28px;font-weight:500}
.about p{position:absolute;left:100px;width:1000px;color:var(--light);font-size:12px;line-height:31px;text-align:center}

/* services */
.services{top:1178px;height:581px;background:var(--white)}
.services h2{position:absolute;top:48px;width:100%;color:var(--ink);font-size:29px}
.services .intro{position:absolute;top:97px;left:110px;width:980px;text-align:center;font-size:12px;line-height:30px;color:var(--muted)}
.svc-photo{position:absolute;top:181px;width:164px;height:164px;margin-left:-82px;border-radius:50%;border:4px solid var(--grey)}
.svc-title{top:365px;font-size:18px;color:var(--ink)}
.svc-text{top:398px;font-size:12px;line-height:26px;color:var(--muted);text-align:justify;text-align-last:center}
.services .btn{top:484px;color:var(--ink);border-color:var(--ink)}

/* news */
.news{top:1759px;height:423px}
.news-bg{position:absolute;inset:0;background:linear-gradient(180deg,#3a3c3e,#252627 60%,#1b1b1b)}
.news-notch{position:absolute;left:584px;top:0}
.news h2{position:absolute;top:58px;width:100%;color:var(--white);font-size:29px;font-weight:500}
.card{position:absolute;top:114px;width:307px;height:309px}
.card-body{height:143px;background:var(--white);padding:18px 22px}
.card .date{font-family:"Fira Sans Condensed",sans-serif;font-size:19px;color:var(--ink);margin-bottom:10px}
.card p{font-size:14px;line-height:23px;color:var(--text)}
.card-photo{height:166px}

/* testimonials */
.reviews{top:2182px;height:375px;background:var(--white)}
.reviews h2{position:absolute;top:42px;width:100%;font-size:29px;color:var(--ink);font-weight:400}
.reviews .quote{position:absolute;top:104px;left:130px;width:940px;text-align:center;font-size:12px;line-height:31px;color:var(--muted)}
.reviews .mark{position:absolute;left:130px;top:96px;font-size:28px;color:var(--grey);font-family:Georgia,serif}
.reviews .name{position:absolute;top:210px;width:100%;font-size:16px;color:var(--ink)}
.avatar{position:absolute;left:569px;top:250px;width:62px;height:62px;border-radius:50%;border:3px solid var(--light)}
.reviews .dots{top:336px;left:565px;gap:10px}
.reviews .dots i{width:9px;height:9px;border:0;background:var(--light)}
.reviews .dots i.on{background:var(--grey)}

/* footer */
.footer{top:2557px;height:183px;background:var(--black);color:var(--light)}
.footer .logo{top:26px;font-size:24px;color:var(--white)}
.footer .logo small{color:var(--white)}
.legal{left:110px;top:70px;font-size:11.5px;color:var(--white)}
.copy{left:110px;top:97px;font-size:11px;color:var(--grey)}
.social{left:110px;top:127px;display:flex;gap:7px}
.social i{width:22px;height:22px;background:var(--grey);border-radius:3px}
.footer h3{font-size:17px;color:var(--white);font-weight:500}
.frow{font-size:11px;color:var(--light);display:flex;align-items:center;gap:7px;white-space:nowrap}
.frow svg{flex:none}
.qlink{font-size:11.5px;color:var(--light)}
</style>
</head>
<body>

<header class="topbar">
  <div class="contact">
    <span><svg width="11" height="11" viewBox="0 0 24 24"><path fill="#dddddd" d="M6.6 10.8a15 15 0 0 0 6.6 6.6l2.2-2.2c.3-.3.7-.4 1-.2 1.1.4 2.3.6 3.6.6.6 0 1 .4 1 1V20c0 .6-.4 1-1 1A17 17 0 0 1 3 4c0-.6.4-1 1-1h3.5c.6 0 1 .4 1 1 0 1.3.2 2.5.6 3.6.1.3 0 .7-.2 1z"/></svg>(123) 456 789 000</span>
    <span><svg width="12" height="10" viewBox="0 0 24 18"><rect x="1" y="1" width="22" height="16" fill="none" stroke="#dddddd" stroke-width="2"/><path d="M1 1l11 9 11-9" fill="none" stroke="#dddddd" stroke-width="2"/></svg>info@vastmereholdings.com.au</span>
  </div>
  <div class="quote-btn">GET A ONLINE QUOTE</div>
</header>

<header class="nav">
  <div class="logo">VASTMERE<small>HOLDINGS</small></div>
  <nav class="menu">
    <span class="active">HOME</span><span>ABOUT US</span><span>SERVICES</span><span>PROJECTS</span><span>CAREERS</span><span>CONTACT US</span>
  </nav>
</header>

<section class="hero">
  <div class="hero-photo" role="img" aria-label="Yellow excavator demolishing a brick building amid rubble"></div>
  <div class="hero-shade"></div>
  <h1 class="head center">Demolition Solutions</h1>
  <div class="dots"><i></i><i class="on"></i><i></i></div>
  <div class="feature-badge head" style="left:267px">
    <svg width="44" height="34" viewBox="0 0 44 34"><path d="M6 26a16 16 0 0 1 32 0z" fill="#fcfcfc"/><rect x="2" y="26" width="40" height="5" rx="2" fill="#fcfcfc"/><rect x="20" y="8" width="4" height="14" fill="#111"/></svg>Safety
  </div>
  <div class="feature-badge head" style="left:601px">
    <svg width="40" height="34" viewBox="0 0 40 34"><path d="M20 32C6 26 4 12 14 2c2 10 12 10 6 30z" fill="#fcfcfc"/><path d="M20 32c14-6 16-20 6-30-2 10-12 10-6 30z" fill="#fcfcfc"/></svg>Environment
  </div>
  <div class="feature-badge head" style="left:933px">
    <svg width="42" height="34" viewBox="0 0 42 34"><circle cx="15" cy="15" r="10" fill="none" stroke="#fcfcfc" stroke-width="6" stroke-dasharray="4 2.5"/><circle cx="15" cy="15" r="4" fill="#fcfcfc"/><circle cx="31" cy="25" r="6" fill="none" stroke="#fcfcfc" stroke-width="4" stroke-dasharray="3 2"/></svg>Support
  </div>
</section>

<section class="features">
  <p class="col abs" style="left:267px">The safety of our clients, workforce and wider community is of paramount importance to Vastmere Transport and Demolition.</p>
  <p class="col abs" style="left:601px">Vastmere Transport &amp; Demolition is committed to reducing the environmental impact of its undertakings. Environmental considerations and deeply...</p>
  <p class="col abs" style="left:933px">Etiam rhoncus, eros ac aliquam efficitur, erat orci dapibus magna, at auctor purus elit eleifend lectus. Fusce nunc lacus, tempus in euismod ac, rhoncus at mi.</p>
  <div class="btn" style="left:267px">MORE</div>
  <div class="btn" style="left:601px">MORE</div>
  <div class="btn" style="left:933px">MORE</div>
</section>

<section class="about">
  <div class="about-bg" role="img" aria-label="Dark broken brick wall background"></div>
  <h2 class="head center">About Us</h2>
  <p style="top:124px">Vastmere Transport Pty Ltd was established by Director Daniel Vastmere in 2002 with a focus providing services within the transport industry. Over time the company has developed and expanded to include the provision of Earthworks and Demolition. Daniel has over 10 years' experience working at all levels within these industries focusing primarily on Demolition and Earthworks in recent times.</p>
  <p style="top:217px">Vastmere Transport and Demolition is built on core values of Service, Safety and Environment and are dedicated to delivering a quality, safe, cost effective, efficient and reliable service.</p>
</section>

<section class="services">
  <h2 class="head center">Services</h2>
  <p class="intro">Vastmere Transport and Demolition offer an extensive range of services including Demolition, Earthworks and Asbestos Removal. We make it our business to consult with clients, assess their needs and tailor a complete solution. We pride ourselves on a professional approach and timely delivery of services.</p>

  <div class="svc-photo" style="left:267px;background:linear-gradient(140deg,#7d95b0,#a88a62 55%,#4d4a46)" role="img" aria-label="Excavator arm tearing down a structure"></div>
  <div class="svc-photo" style="left:601px;background:linear-gradient(140deg,#d8d6d0,#b1aca3 55%,#7a756e)" role="img" aria-label="Worker breaking concrete with a jackhammer"></div>
  <div class="svc-photo" style="left:933px;background:linear-gradient(140deg,#c9b8a2,#8e6e4f 50%,#3f5a45)" role="img" aria-label="Worker in hard hat removing ceiling sheets"></div>

  <div class="col abs head svc-title" style="left:267px">Demolition</div>
  <div class="col abs head svc-title" style="left:601px">Earthworks</div>
  <div class="col abs head svc-title" style="left:933px">Asbestos</div>

  <p class="col abs svc-text" style="left:267px">Vastmere Transport and Demolition offer an extensive range of services including Demolition, Earthworks and Asbestos Removal.</p>
  <p class="col abs svc-text" style="left:601px">Vastmere Transport and Demolition possess all necessary equipment and skilled personnel to provide earthmoving services</p>
  <p class="col abs svc-text" style="left:933px">Asbestos is a naturally occurring silicate mineral made up of tiny fibres. When disturbed, it may produce a dust containing asbestos fibres.</p>

  <div class="btn" style="left:267px">MORE</div>
  <div class="btn" style="left:601px">MORE</div>
  <div class="btn" style="left:933px">MORE</div>
</section>

<section class="news">
  <div class="news-bg" role="img" aria-label="City skyline over a demolition site"></div>
  <svg class="news-notch" width="32" height="28" viewBox="0 0 32 28"><path d="M0 0h32L16 28z" fill="#fcfcfc"/></svg>
  <h2 class="head center">Latest News</h2>
  <article class="card" style="left:111px">
    <div class="card-body"><div class="date">24/11/2015</div><p>Ut wisi enim ad minim veniam, quis no strud exerci tation ullamcorper suscipit lobortis</p></div>
    <div class="card-photo" style="background:linear-gradient(160deg,#9a9388,#6f665b 60%,#3c3631)" role="img" aria-label="Partly demolished brick house"></div>
  </article>
  <article class="card" style="left:446px">
    <div class="card-body"><div class="date">23/11/2015</div><p>Lorem ipsum dolor sit amet, conse cte tuer adipiscing elit, sed diam nonummy nibh euismod</p></div>
    <div class="card-photo" style="background:linear-gradient(160deg,#a1876a,#c4a15a 45%,#5e4c3e)" role="img" aria-label="Excavator working against a brick wall"></div>
  </article>
  <article class="card" style="left:780px">
    <div class="card-body"><div class="date">20/11/2015</div><p>Duis autem vel eum iriure dolor in hendr erit in vulputate velit esse mole stie conse quat, vel illum dolore</p></div>
    <div class="card-photo" style="background:linear-gradient(160deg,#c2c2c0,#8a8780 50%,#4b4a47)" role="img" aria-label="Yellow excavator on a rubble pile"></div>
  </article>
</section>

<section class="reviews">
  <h2 class="head center">What Our Customers Say About Us</h2>
  <span class="mark">&ldquo;</span>
  <p class="quote">Nam liber tempor cum soluta nobis eleifend option congue nihil imperdiet doming id quod mazim placerat facer possim assum. Typi non habent claritatem insitam; est usus legentis in iis qui facit eorum claritatem. Investigationes demonstraverunt lectores legere me lius quod ii legunt saepius. Claritas est etiam processus dynamicus, qui sequitur mutationem consuetudium lectorum. Mirum est notare quam littera gothica, quam nunc putamus parum claram.</p>
  <div class="name head center">Liam Carter &ndash; Location</div>
  <div class="avatar" style="background:linear-gradient(150deg,#8aa0a8,#4e5a60)" role="img" aria-label="Customer portrait"></div>
  <div class="dots"><i></i><i></i><i class="on"></i><i></i></div>
</section>

<footer class="footer" style="position:absolute;left:0;width:1200px">
  <div class="logo">VASTMERE<small>HOLDINGS</small></div>
  <div class="abs legal">Privacy Policy &nbsp;|&nbsp; Sitemap</div>
  <div class="abs copy">Copyrights &copy; 2015 Vastmere Holdings. All Right Reserved.</div>
  <div class="abs social"><i></i><i></i><i></i><i></i><i></i></div>

  <h3 class="abs head" style="left:447px;top:32px">Contact</h3>
  <div class="abs frow" style="left:447px;top:66px"><svg width="10" height="10" viewBox="0 0 10 10"><circle cx="5" cy="3" r="2.5" fill="#ddd"/><path d="M0 10a5 5 0 0 1 10 0z" fill="#ddd"/></svg>Daniel Vastmere (Director)</div>
  <div class="abs frow" style="left:447px;top:92px"><svg width="10" height="10" viewBox="0 0 10 10"><rect width="10" height="10" rx="2" fill="#ddd"/></svg>0400 555 118</div>
  <div class="abs frow" style="left:447px;top:114px"><svg width="10" height="8" viewBox="0 0 10 8"><rect width="10" height="8" fill="#ddd"/></svg>vtdemolition@vastmail.com</div>
  <div class="abs frow" style="left:447px;top:140px"><svg width="8" height="11" viewBox="0 0 8 11"><path d="M4 11C1 7 0 5.5 0 4a4 4 0 0 1 8 0c0 1.5-1 3-4 7z" fill="#ddd"/></svg>PO Box 512 KELLAWAY QLD 4391</div>

  <div class="abs frow" style="left:677px;top:66px"><svg width="10" height="10" viewBox="0 0 10 10"><circle cx="5" cy="3" r="2.5" fill="#ddd"/><path d="M0 10a5 5 0 0 1 10 0z" fill="#ddd"/></svg>Mira Tolland (Administration)</div>
  <div class="abs frow" style="left:677px;top:92px"><svg width="10" height="10" viewBox="0 0 10 10"><rect width="10" height="10" rx="2" fill="#ddd"/></svg>0400 555 274</div>
  <div class="abs frow" style="left:677px;top:114px"><svg width="10" height="8" viewBox="0 0 10 8"><rect width="10" height="8" fill="#ddd"/></svg>vtdemolition@vastmail.com</div>
  <div class="abs frow" style="left:677px;top:140px"><svg width="8" height="11" viewBox="0 0 8 11"><path d="M4 11C1 7 0 5.5 0 4a4 4 0 0 1 8 0c0 1.5-1 3-4 7z" fill="#ddd"/></svg>PO Box 512 KELLAWAY QLD 4391</div>

  <h3 class="abs head" style="left:906px;top:32px">Quick Links</h3>
  <div class="abs qlink" style="left:906px;top:70px">&raquo; Services</div>
  <div class="abs qlink" style="left:906px;top:100px">&raquo; Projects</div>
  <div class="abs qlink" style="left:906px;top:130px">&raquo; News</div>
  <div class="abs qlink" style="left:992px;top:70px">&raquo; Career</div>
  <div class="abs qlink" style="left:992px;top:100px">&raquo; Contact Us</div>
  <div class="abs qlink" style="left:992px;top:130px">&raquo; Sitemap</div>
</footer>

</body>
</html>
```